Quill And Ferry Business Card

I need a business card designed around my logo (which was designed here on Sketch Forum!)

Target Market(s)

Professional Businesses

Industry/Entity Type

Business

Requirements
Must have
• Details that must be on the business card:

Renata Ovalle
Director
0491 253 608
renata@quillandferry.com.au
www.quillandferry.com.au
PO Box 4720 Larkfield Vic 3912

```html
<!DOCTYPE html>
<html lang="en">
<head>
<meta charset="utf-8">
<title>Quill And Ferry Business Card</title>
<link rel="stylesheet" href="https://fonts.googleapis.com/css2?family=Marcellus&family=Questrial&family=Mulish:wght@800&display=swap">
<style>
  :root {
    --backdrop: #2f2f31;
    --paper: #e6e6e4;
    --charcoal: #2b2b2c;
    --ink: #333335;
    --red: #a3141c;
    --silver: #d9d9d9;
  }
  * { box-sizing: border-box; margin: 0; padding: 0; }
  html, body { width: 1200px; height: 900px; overflow: hidden; }
  body {
    background: var(--backdrop);
    font-family: "Questrial", sans-serif;
    position: relative;
  }
  .card {
    position: absolute;
    left: 250px;
    width: 700px;
    height: 400px;
    overflow: hidden;
  }
  .card--front { top: 40px; background: var(--paper); color: var(--ink); }
  .card--back { top: 470px; background: var(--charcoal); color: var(--silver); }

  .brand { position: absolute; display: flex; align-items: center; gap: 18px; }
  .brand__mark { width: 46px; height: 46px; background: var(--red); flex: none; }
  .brand__name {
    font-family: "Marcellus", serif;
    font-size: 44px;
    letter-spacing: 1px;
    text-transform: uppercase;
    line-height: 1;
    white-space: nowrap;
  }
  .tagline {
    position: absolute;
    font-family: "Marcellus", serif;
    text-transform: uppercase;
    letter-spacing: 5px;
    line-height: 1;
    white-space: nowrap;
  }
  .card--front .brand { left: 120px; top: 70px; }
  .card--front .brand__name { color: var(--ink); }
  .card--front .tagline { left: 184px; top: 124px; font-size: 19px; color: var(--red); }

  .person { position: absolute; left: 56px; top: 190px; }
  .person__name {
    font-family: "Mulish", sans-serif;
    font-weight: 800;
    font-size: 20px;
    color: var(--red);
    text-transform: uppercase;
  }
  .person__role { font-size: 16px; color: var(--ink); margin-top: 2px; }

  .contact {
    position: absolute;
    right: 40px;
    top: 270px;
    text-align: right;
    font-size: 16px;
    line-height: 1.6;
    color: var(--ink);
  }
  .contact__label { color: var(--red); }

  .band { position: absolute; left: 0; bottom: 0; width: 700px; height: 36px; }

  .card--back .brand { left: 60px; top: 150px; }
  .card--back .brand__mark { width: 80px; height: 80px; }
  .card--back .brand__name { color: var(--silver); font-size: 46px; }
  .card--back .tagline { left: 158px; top: 218px; font-size: 19px; color: var(--red); }
  .website { position: absolute; right: 44px; bottom: 52px; font-size: 18px; color: var(--silver); }
</style>
</head>
<body>

<section class="card card--front">
  <div class="brand">
    <span class="brand__mark"></span>
    <span class="brand__name">Quill And Ferry</span>
  </div>
  <p class="tagline">Accounts Kept Simple</p>

  <div class="person">
    <p class="person__name">Renata Ovalle</p>
    <p class="person__role">Director</p>
  </div>

  <div class="contact">
    <p>PO Box 4720 Larkfield Vic 3912</p>
    <p><span class="contact__label">T:</span> 0491 253 608 · <span class="contact__label">E:</span> renata@quillandferry.com.au</p>
  </div>

  <svg class="band" viewBox="0 0 700 36" aria-hidden="true">
    <polygon points="0,0 230,0 250,36 0,36" fill="var(--red)"/>
    <polygon points="238,0 700,0 700,36 258,36" fill="var(--charcoal)"/>
  </svg>
</section>

<section class="card card--back">
  <div class="brand">
    <span class="brand__mark"></span>
    <span class="brand__name">Quill And Ferry</span>
  </div>
  <p class="tagline">Accounts Kept Simple</p>
  <p class="website">www.quillandferry.com.au</p>
</section>

</body>
</html>
```